Personal Training

Personal Fitness Trainer
Sports Nutritionist
Individual and Group rates available
Certifications
Global Wellness Coaching Federation
Continental Athletic Studies Council

Industry/Entity Type

Fitness

Contact Information for Business Card

Dorinda Pellham
555-284-7163
vetrubel4@quintmail.example

```html
<!DOCTYPE html>
<html lang="en">
<head>
<meta charset="utf-8">
<title>Dorinda Pellham – Personal Training Business Card</title>
<link rel="stylesheet" href="https://fonts.googleapis.com/css2?family=Quicksand:wght@500;600;700&display=swap">
<style>
  :root {
    --page-bg: #ece9e4;
    --card-dark: #1e1e21;
    --card-dark-edge: #0c0c0e;
    --metal-light: #d9d9dc;
    --metal-mid: #a9a9ae;
    --metal-dark: #7d7d83;
    --violet: #9c7bd0;
    --violet-deep: #8566bd;
    --violet-text: #8e6cc6;
    --photo-violet: #6f6890;
    --photo-light: #c9c4d8;
    --paper: #f7f7f8;
    --ink: #2b2b30;
    --white: #ffffff;
    --badge-red: #c8383d;
    --badge-blue: #2f6fb5;
    --badge-gray: #55555c;
  }
  * { box-sizing: border-box; margin: 0; padding: 0; }
  html, body {
    width: 1200px; height: 1000px; overflow: hidden;
    background: var(--page-bg);
    font-family: "Quicksand", "Helvetica Neue", Arial, sans-serif;
  }
  .canvas { position: relative; width: 1200px; height: 1000px; }
  .card {
    position: absolute; left: 170px; width: 860px; height: 470px;
    overflow: hidden; border-radius: 4px;
    box-shadow: 0 10px 28px rgba(0,0,0,0.22);
  }

  /* Front */
  .card-front {
    top: 22px;
    background: radial-gradient(ellipse at 60% 40%, #2c2c31 0%, var(--card-dark) 55%, var(--card-dark-edge) 100%);
  }
  .front-portrait {
    position: absolute; left: 40px; top: 30px; width: 210px; height: 410px;
    border-radius: 6px;
    background: linear-gradient(180deg, #b98a6e 0%, #8f5a48 45%, #3d3346 80%, #2a2530 100%);
    box-shadow: 0 0 22px rgba(255,255,255,0.55);
  }
  .front-band { position: absolute; left: 250px; right: 0; top: 120px; height: 230px; }
  .band-stripe-top {
    position: absolute; left: 0; right: 0; top: 0; height: 62px;
    background: var(--violet);
    display: flex; align-items: center; padding-left: 40px;
  }
  .band-metal {
    position: absolute; left: 0; right: 0; top: 62px; height: 154px;
    background:
      repeating-linear-gradient(90deg, rgba(255,255,255,0.12) 0 2px, rgba(0,0,0,0.05) 2px 5px),
      linear-gradient(100deg, var(--metal-dark) 0%, var(--metal-light) 45%, var(--metal-mid) 100%);
    padding: 26px 0 0 40px;
  }
  .band-stripe-bottom {
    position: absolute; left: 0; right: 0; bottom: 0; height: 14px;
    background: var(--violet-deep);
  }
  .holder-name { color: var(--white); font-weight: 700; font-size: 36px; letter-spacing: 0.5px; }
  .contact-line {
    color: var(--white); font-weight: 600; font-size: 30px; line-height: 1.5;
    text-shadow: 0 1px 2px rgba(0,0,0,0.25);
  }

  /* Back */
  .card-back { top: 510px; background: var(--paper); }
  .back-photo {
    position: absolute; left: 0; top: 0; width: 100%; height: 180px;
    background: linear-gradient(120deg, var(--photo-violet) 0%, #8c87a6 45%, var(--photo-light) 100%);
  }
  .services {
    position: absolute; left: 300px; top: 194px; width: 500px;
    color: var(--violet-text); font-weight: 700; font-size: 25px; line-height: 28px;
  }
  .cert-label {
    position: absolute; left: 0; top: 316px; width: 620px; height: 40px;
    background: var(--violet);
    color: var(--white); font-weight: 700; font-size: 25px;
    display: flex; align-items: center; padding-left: 300px;
  }
  .cert-list {
    position: absolute; left: 40px; top: 366px;
    color: var(--ink); font-weight: 600; font-size: 17px; line-height: 22px;
    list-style: none;
  }
  .badges {
    position: absolute; left: 40px; top: 418px; display: flex; gap: 60px; align-items: center;
  }
  .accent-rule {
    position: absolute; right: 0; top: 316px; width: 36px; height: 154px; background: var(--violet);
  }
</style>
</head>
<body>
<main class="canvas">

  <section class="card card-front" aria-label="Business card front">
    <div class="front-portrait" role="img" aria-label="Photo of the trainer posing in athletic wear"></div>
    <div class="front-band">
      <div class="band-stripe-top"><h1 class="holder-name">Dorinda Pellham</h1></div>
      <div class="band-metal">
        <p class="contact-line">555-284-7163</p>
        <p class="contact-line">vetrubel4@quintmail.example</p>
      </div>
      <div class="band-stripe-bottom"></div>
    </div>
  </section>

  <section class="card card-back" aria-label="Business card back">
    <div class="back-photo" role="img" aria-label="Black and white photo of a trainer working out at a gym machine, tinted violet"></div>
    <div class="services">
      <p>Personal Fitness Trainer</p>
      <p>Sports Nutritionist</p>
      <p>Individual and Group</p>
      <p>rates available</p>
    </div>
    <div class="cert-label">Certifications</div>
    <ul class="cert-list">
      <li>Global Wellness Coaching Federation</li>
      <li>Continental Athletic Studies Council</li>
    </ul>
    <div class="badges">
      <svg width="90" height="40" viewBox="0 0 90 40" role="img" aria-label="Certification badge">
        <rect x="0" y="0" width="90" height="40" rx="5" fill="var(--badge-gray)"/>
      </svg>
      <svg width="84" height="40" viewBox="0 0 84 40" role="img" aria-label="Certification badge">
        <rect x="0" y="0" width="38" height="40" fill="var(--badge-red)"/>
        <rect x="42" y="0" width="42" height="40" fill="var(--badge-blue)"/>
      </svg>
    </div>
    <div class="accent-rule"></div>
  </section>

</main>
</body>
</html>
```